Merrowind Flyer

A simple flyer that gets people attention
I have a attached a sample of what we use now and a picture we use
We service gas fireplaces and need a eye catching but not to cluttered flyer to promote our business. the cost per fireplace should be $60.00

Reason: Sorry for the delay We are out of town on holidays with sketchy internet service To frustrating to complete this project till I am back in a week Thank you for your patience Kind regards Dale

```html
<!DOCTYPE html>
<html lang="en">
<head>
<meta charset="utf-8">
<title>Merrowind Gas Services Flyer</title>
<link rel="stylesheet" href="https://fonts.googleapis.com/css2?family=Open+Sans:ital,wght@0,300;0,400;0,600;0,700;1,400;1,600&display=swap">
<style>
:root{
  --bg:#3b3b3b;
  --dark:#221f1e;
  --rust:#a8461f;
  --rust-deep:#7d3214;
  --rust-light:#c0602f;
  --white:#ffffff;
  --grey:#6c6c6c;
  --text-light:#e9e4e0;
  --photo-a:#2a1710;
  --photo-b:#6b3620;
  --photo-c:#c9793f;
}
*{margin:0;padding:0;box-sizing:border-box}
html,body{width:1200px;height:772px;overflow:hidden}
body{background:var(--bg);font-family:'Open Sans',Arial,sans-serif;position:relative}
.flyer{position:absolute;top:80px;width:473px;height:612px;background:var(--white);overflow:hidden}
.flyer--classic{left:113px}
.flyer--overlay{left:636px}
.photo{position:absolute;left:0;top:0;width:100%;
  background:radial-gradient(ellipse at 55% 30%,var(--photo-c) 0%,var(--photo-b) 35%,var(--photo-a) 75%)}
.flyer--classic .photo{height:308px}
.flyer--overlay .photo{height:357px}
.headline{position:absolute;color:var(--white)}
.headline h1{font-weight:600;font-size:22px;line-height:1.15;letter-spacing:.3px}
.headline p{font-style:italic;font-size:13px;margin-top:6px}
.flyer--classic .headline{left:0;right:0;top:24px;text-align:center}
.flyer--overlay .headline{left:18px;top:16px}
.flyer--overlay .headline h1{font-size:19px;line-height:1.3}
.band{position:absolute;left:0;width:100%;height:50px;
  background:linear-gradient(90deg,rgba(125,50,20,.92),rgba(192,96,47,.85));
  display:flex;align-items:center;color:var(--white)}
.flyer--classic .band{top:258px}
.flyer--overlay .band{top:305px;height:52px}
.brand{font-size:19px;font-weight:300;padding-left:18px;width:302px;letter-spacing:.1px;white-space:nowrap}
.brand b{font-weight:700}
.divider{width:1px;height:34px;background:rgba(255,255,255,.7)}
.price{display:flex;align-items:center;padding-left:18px}
.price strong{font-size:26px;font-weight:700}
.price span{font-size:8.5px;line-height:1.15;margin-left:6px}
.price em{font-style:italic}
.notice{position:absolute;left:0;width:100%;background:var(--dark);color:var(--text-light);
  padding:18px 18px 0;font-size:7.6px;line-height:1.35;text-align:justify}
.flyer--classic .notice{top:308px;height:112px}
.flyer--overlay .notice{top:357px;height:199px;padding-top:22px}
.notice p{margin-bottom:6px}
.notice .legal{color:#8f8a86;font-style:italic;font-size:6.6px;margin-top:12px}
.info{position:absolute;left:18px;top:440px;width:262px}
.legal-light{color:var(--grey);font-style:italic;font-size:6.4px;line-height:1.35;text-align:justify}
.contact-lead{color:var(--rust);font-style:italic;font-weight:600;font-size:6.8px;margin-top:22px}
.phone{color:var(--rust);font-weight:700;font-size:20px;line-height:1.2}
.email{color:var(--rust);font-weight:600;font-size:6.8px;margin-top:6px}
.terms{color:var(--grey);font-style:italic;font-size:6.2px;line-height:1.35;margin-top:2px}
.signs{position:absolute;background:var(--rust);color:var(--white);padding:14px 12px}
.flyer--classic .signs{left:296px;top:437px;width:156px;height:175px}
.flyer--overlay .signs{left:301px;top:0;width:172px;height:175px;background:rgba(168,70,31,.9);padding-top:16px}
.signs h2{font-size:6.6px;font-weight:600;line-height:1.45;margin-bottom:8px}
.signs ol{list-style:none;font-size:6.4px;line-height:1.25}
.signs li{display:flex;margin-bottom:3px}
.signs li span{width:16px;flex:none}
.footer{position:absolute;left:0;top:556px;width:100%;height:56px;padding:8px 18px;display:flex;justify-content:space-between}
.footer .contact-lead{margin-top:0}
.footer .right{text-align:right}
.footer .email{margin-top:0}
</style>
</head>
<body>

<section class="flyer flyer--classic">
  <div class="photo" role="img" aria-label="Photo of a family's bare feet warming in front of a glowing gas fireplace"></div>
  <div class="headline">
    <h1>NOTICE TO THE OWNERS</h1>
    <p>NAME OF PROPERTY</p>
  </div>
  <div class="band">
    <div class="brand"><b>MERROWIND</b> GAS SERVICES</div>
    <div class="divider"></div>
    <div class="price"><strong>$60</strong><span>cost per fireplace<br><em>(tax included)</em></span></div>
  </div>
  <div class="notice">
    <p>MERROWIND GAS SERVICES WILL BE ON SITE CONDUCTING GAS FIREPLACE SAFETY INSPECTIONS AND MAINTENANCE FOR NAME OF PROPERTY ON DATE OF SERVICE.</p>
    <p>If you wish to have your fireplace serviced, please put your name and unit number on the sign-up sheet provided. We will require approximately 20 - 30 minutes to service each fireplace and require that the fireplace is cool to conduct the work.</p>
    <p>PLEASE DO NOT USE YOUR FIREPLACE WITHIN 2 HOURS OF YOUR APPOINTMENT AS WE DO NOT WANT THE TECHNICIANS TO RECEIVE BURNS.</p>
  </div>
  <div class="info">
    <p class="legal-light">The National Home Energy Safety Council states that all fireplaces require regular servicing. Fireplace manufacturers recommend each unit be serviced annually by a qualified technician and insurance companies and Fire Departments are now asking for reports regarding fireplace safety inspections and servicing. The service Merrowind Gas Services will provide will entail a thorough assessment of pilot, burner and valve operation, a door seal inspection, an inspection of the electrical circuits, repositioning of the logs, cleaning and adjustment of fan and controls, cleaning of the firebox and glass, a carbon monoxide test, testing of fittings for gas leaks and a complete operational test once the service is complete.</p>
    <p class="contact-lead">For further information please contact Nadia at:</p>
    <p class="phone">604.555.0187</p>
    <p class="email">You may also email us at: nadia.merrowindgas@example.com</p>
    <p class="terms">(Owners must have payment ready at time of inspection.<br>Payment may be made in the form of cash, cheque, debit or credit card)</p>
  </div>
  <aside class="signs">
    <h2>POSSIBLE INDICATION THAT YOUR GAS FIREPLACE REQUIRES SERVICE INCLUDE:</h2>
    <ol>
      <li><span>(1)</span>Cloudy film on glass</li>
      <li><span>(2)</span>Strong odors when fireplace is in operation</li>
      <li><span>(3)</span>Soot build up on glass, logs or exterior of building</li>
      <li><span>(4)</span>Tarnished/discolored brass</li>
      <li><span>(5)</span>Pilot light outages</li>
      <li><span>(6)</span>Main burner is not lighting consistently</li>
      <li><span>(7)</span>Delayed ignition</li>
      <li><span>(8)</span>Flames are not evenly dispersed.</li>
    </ol>
  </aside>
</section>

<section class="flyer flyer--overlay">
  <div class="photo" role="img" aria-label="Photo of a family's bare feet warming in front of a glowing gas fireplace"></div>
  <div class="headline">
    <h1>NOTICE TO<br>THE OWNERS</h1>
    <p>NAME OF PROPERTY</p>
  </div>
  <aside class="signs">
    <h2>POSSIBLE INDICATION THAT YOUR GAS FIREPLACE REQUIRES SERVICE INCLUDE:</h2>
    <ol>
      <li><span>(1)</span>Cloudy film on glass</li>
      <li><span>(2)</span>Strong odors when fireplace is in operation</li>
      <li><span>(3)</span>Soot build up on glass, logs or exterior of building</li>
      <li><span>(4)</span>Tarnished/discolored brass</li>
      <li><span>(5)</span>Pilot light outages</li>
      <li><span>(6)</span>Main burner is not lighting consistently</li>
      <li><span>(7)</span>Delayed ignition</li>
      <li><span>(8)</span>Flames are not evenly dispersed.</li>
    </ol>
  </aside>
  <div class="band">
    <div class="brand"><b>MERROWIND</b> GAS SERVICES</div>
    <div class="divider"></div>
    <div class="price"><strong>$60</strong><span>cost per fireplace<br><em>(tax included)</em></span></div>
  </div>
  <div class="notice">
    <p>MERROWIND GAS SERVICES WILL BE ON SITE CONDUCTING GAS FIREPLACE SAFETY INSPECTIONS AND MAINTENANCE FOR NAME OF PROPERTY ON DATE OF SERVICE.</p>
    <p>If you wish to have your fireplace serviced, please put your name and unit number on the sign-up sheet provided. We will require approximately 20 - 30 minutes to service each fireplace and require that the fireplace is cool to conduct the work.</p>
    <p>PLEASE DO NOT USE YOUR FIREPLACE WITHIN 2 HOURS OF YOUR APPOINTMENT AS WE DO NOT WANT THE TECHNICIANS TO RECEIVE BURNS.</p>
    <p class="legal">The National Home Energy Safety Council states that all fireplaces require regular servicing. Fireplace manufacturers recommend each unit be serviced annually by a qualified technician and insurance companies and Fire Departments are now asking for reports regarding fireplace safety inspections and servicing. The service Merrowind Gas Services will provide will entail a thorough assessment of pilot, burner and valve operation, a door seal inspection, an inspection of the electrical circuits, repositioning of the logs, cleaning and adjustment of fan and controls, cleaning of the firebox and glass, a carbon monoxide test, testing of fittings for gas leaks and a complete operational test once the service is complete.</p>
  </div>
  <div class="footer">
    <div>
      <p class="contact-lead">For further information please contact Nadia at:</p>
      <p class="phone">604.555.0187</p>
    </div>
    <div class="right">
      <p class="email">You may also email us at: nadia.merrowindgas@example.com</p>
      <p class="terms">(Owners must have payment ready at time of inspection.<br>Payment may be made in the form of cash, cheque, debit or credit card)</p>
    </div>
  </div>
</section>

</body>
</html>
```